Electrician Business needs flyer for discount offer and advertise services

Need a promotional flyer that will grab attention,, offer:

During the months of October & November receive a 10% discount on;
Ceiling fan installation
Smoke alarm installation
Replace existing downlights for new LED downlights.
Offer expires 30th November 2016
'Keep cool, stay safe and save power with VoltMate'

Would like to advertise services and quality on reverse-side. Can have graphic pointing to reverse side on both sides, encouraging customer to read both sides of flyer.
Contact details both sides
Design to suit two-sided A5

Reverse side list services;

All residential & commercial electrical services
Electrical contracting
Real estate/strata electrical maintenance & repairs
New builds
Renovations
Security sensor lighting
Ceiling fans
Smoke Alarms
Data connections

Target Market(s)

Residential home owners and commercial, building and construction companies

Industry/Entity Type

Electrical

Font styles to use
Serif

Colors
0255a3
ffffff

Requirements
Nice to have
• A picture of a modern ceiling fan.
• Arrow/graphic pointing to reverse side, so customer reads both sides of flyer

```html
<!DOCTYPE html>
<html lang="en">
<head>
<meta charset="utf-8">
<title>VoltMate – Services</title>
<link rel="stylesheet" href="https://fonts.googleapis.com/css2?family=Alfa+Slab+One&family=Anton&display=swap">
<style>
  :root {
    --navy: #2a2b8c;
    --navy-deep: #24247a;
    --brand-blue: #0255a3;
    --band-blue: #1f7fd6;
    --stripe-blue: #3fa4ec;
    --sky: #58c3f2;
    --yellow: #ffe600;
    --white: #ffffff;
  }
  * { margin: 0; padding: 0; box-sizing: border-box; }
  html, body { width: 849px; height: 1200px; overflow: hidden; background: var(--navy); }
  .flyer {
    position: relative;
    width: 849px;
    height: 1200px;
    overflow: hidden;
    background: var(--navy);
    font-family: "Alfa Slab One", Georgia, serif;
  }
  .fan-backdrop {
    position: absolute;
    inset: 0;
    background:
      radial-gradient(ellipse 430px 300px at 300px 330px, rgba(88,195,242,0.35), transparent 70%),
      radial-gradient(ellipse 380px 420px at 560px 760px, rgba(40,140,220,0.45), transparent 72%),
      radial-gradient(ellipse 300px 260px at 120px 900px, rgba(60,120,210,0.35), transparent 70%),
      linear-gradient(160deg, var(--navy) 0%, #2b3a9c 45%, var(--navy-deep) 100%);
  }
  .page-turn { position: absolute; left: 0; top: 0; width: 200px; height: 200px; }
  .brand {
    position: absolute;
    right: 40px;
    top: 82px;
    display: flex;
    align-items: center;
    gap: 16px;
    color: var(--white);
    font-size: 70px;
    line-height: 1;
  }
  .brand-dot { width: 30px; height: 30px; border-radius: 50%; background: var(--white); }
  .services {
    position: absolute;
    left: 0;
    right: 0;
    top: 230px;
    list-style: none;
    text-align: center;
    color: var(--yellow);
    font-size: 43px;
    line-height: 69.8px;
  }
  .services li { white-space: nowrap; }
  .bolt { display: inline-block; width: 24px; height: 38px; margin-right: 14px; vertical-align: -4px; }
  .services .continued { padding-left: 40px; }
  .call-band { position: absolute; left: 170px; top: 1036px; width: 679px; height: 134px; }
  .call-band-shape { position: absolute; left: 0; top: 0; width: 679px; height: 134px; }
  .call-label {
    position: absolute;
    left: 82px;
    top: 35px;
    font-family: "Anton", "Arial Narrow", sans-serif;
    color: var(--yellow);
    font-size: 30px;
    line-height: 32px;
    white-space: nowrap;
  }
  .call-icon { position: absolute; left: 166px; top: 34px; width: 72px; height: 72px; }
  .call-number {
    position: absolute;
    left: 244px;
    top: 0;
    height: 134px;
    font-family: "Anton", "Arial Narrow", sans-serif;
    color: var(--yellow);
    font-size: 78px;
    line-height: 134px;
    white-space: nowrap;
  }
</style>
</head>
<body>
<main class="flyer">
  <div class="fan-backdrop" role="img" aria-label="Soft blue photo of a modern ceiling fan filling the background"></div>

  <svg class="page-turn" viewBox="0 0 200 200" aria-hidden="true">
    <path d="M0 0 H190 L0 180 Z" fill="#ffffff"/>
    <path d="M190 0 C150 60 110 110 0 180 C60 160 120 150 175 150 C160 110 170 50 190 0 Z" fill="var(--sky)"/>
    <path d="M190 0 C168 55 160 105 175 150 C150 120 140 70 190 0 Z" fill="#2f8fd8"/>
    <path d="M30 112 C36 62 80 36 128 52 L134 34 L170 86 L112 100 L120 80 C88 70 58 82 48 116 Z" fill="var(--yellow)"/>
  </svg>

  <div class="brand"><span class="brand-dot"></span><span>VoltMate</span></div>

  <ul class="services">
    <li><svg class="bolt" viewBox="0 0 24 38"><path d="M14 0 L2 22 H11 L8 38 L22 14 H13 L18 0 Z" fill="var(--yellow)"/></svg>All residential &amp; commercial</li>
    <li class="continued">electrical services</li>
    <li><svg class="bolt" viewBox="0 0 24 38"><path d="M14 0 L2 22 H11 L8 38 L22 14 H13 L18 0 Z" fill="var(--yellow)"/></svg>Electrical contracting</li>
    <li><svg class="bolt" viewBox="0 0 24 38"><path d="M14 0 L2 22 H11 L8 38 L22 14 H13 L18 0 Z" fill="var(--yellow)"/></svg>Real estate/strata electrical</li>
    <li class="continued">maintenance &amp; repairs</li>
    <li><svg class="bolt" viewBox="0 0 24 38"><path d="M14 0 L2 22 H11 L8 38 L22 14 H13 L18 0 Z" fill="var(--yellow)"/></svg>New builds</li>
    <li><svg class="bolt" viewBox="0 0 24 38"><path d="M14 0 L2 22 H11 L8 38 L22 14 H13 L18 0 Z" fill="var(--yellow)"/></svg>Renovations</li>
    <li><svg class="bolt" viewBox="0 0 24 38"><path d="M14 0 L2 22 H11 L8 38 L22 14 H13 L18 0 Z" fill="var(--yellow)"/></svg>Security sensor lighting</li>
    <li><svg class="bolt" viewBox="0 0 24 38"><path d="M14 0 L2 22 H11 L8 38 L22 14 H13 L18 0 Z" fill="var(--yellow)"/></svg>Ceiling fans</li>
    <li><svg class="bolt" viewBox="0 0 24 38"><path d="M14 0 L2 22 H11 L8 38 L22 14 H13 L18 0 Z" fill="var(--yellow)"/></svg>Smoke Alarms</li>
    <li><svg class="bolt" viewBox="0 0 24 38"><path d="M14 0 L2 22 H11 L8 38 L22 14 H13 L18 0 Z" fill="var(--yellow)"/></svg>Data connections</li>
  </ul>

  <div class="call-band">
    <svg class="call-band-shape" viewBox="0 0 679 134" preserveAspectRatio="none" aria-hidden="true">
      <path d="M14 0 H42 L28 134 H0 Z" fill="var(--stripe-blue)"/>
      <path d="M56 0 H679 V134 H42 Z" fill="var(--band-blue)"/>
    </svg>
    <div class="call-label">CALL<br>NOW</div>
    <svg class="call-icon" viewBox="0 0 72 72" aria-hidden="true">
      <circle cx="36" cy="36" r="34" fill="#ffffff"/>
      <path d="M24 18 L30 17 L34 27 L29 31 C31 37 35 41 41 43 L45 38 L55 42 L54 48 C52 53 47 55 42 53 C30 49 23 42 19 30 C17 25 19 20 24 18 Z" fill="var(--brand-blue)"/>
      <path d="M40 22 A12 12 0 0 1 50 32" stroke="var(--brand-blue)" stroke-width="3" fill="none" stroke-linecap="round"/>
      <path d="M41 14 A20 20 0 0 1 58 31" stroke="var(--brand-blue)" stroke-width="3" fill="none" stroke-linecap="round"/>
    </svg>
    <div class="call-number">XXX-XXX-XXXX</div>
  </div>
</main>
</body>
</html>
```